Healthcare and Professional IT Services Company need a redesigned business card

We are a IT Services company that targets small medical practices and professional business such as Attorneys, Accounts, Architects etc. We want to communicate a professional yet friendly image using recent logo redesign here on Drafthive. Like to see the colors blue and orange in the design. Must use the Tall Cedar Technology as displayed in the new logo - then also want to incorporate the fish logo as well.

Target Market(s)

Small medical and professional services

Industry/Entity Type

It Company

Contact Information for Business Card

The usual stuff, place for name address phone website. Also maybe our tagline which is "hooked on technology"

Requirements
Must have
• My new logo and the fish somewhere on the card

```html
<!DOCTYPE html>
<html lang="en">
<head>
<meta charset="utf-8">
<title>Tall Cedar Technology – Business Card</title>
<link href="https://fonts.googleapis.com/css2?family=Merriweather:wght@400&display=swap" rel="stylesheet">
<style>
  :root {
    --page: #e9e6e1;
    --card-white: #f7f8f8;
    --blue-light: #1fb0e3;
    --blue-deep: #0a78b8;
    --brand-blue: #2bb3e0;
    --ink-white: #ffffff;
    --card-black: #0b0b0c;
    --shadow: rgba(0,0,0,0.22);
  }
  * { box-sizing: border-box; margin: 0; padding: 0; }
  html, body { width: 1200px; height: 892px; overflow: hidden; }
  body {
    background: var(--page);
    font-family: "Merriweather", Georgia, serif;
    position: relative;
  }
  .card {
    position: absolute;
    top: 296px;
    width: 525px;
    height: 300px;
    border-radius: 3px;
    overflow: hidden;
    box-shadow: 0 10px 26px var(--shadow);
  }
  .card--front { left: 50px; background: var(--card-white); }
  .card--back  { left: 625px; background: var(--card-black); }

  /* front: logo side */
  .front__logo-side {
    position: absolute; left: 0; top: 0; width: 205px; height: 100%;
    display: flex; flex-direction: column; align-items: center; justify-content: center;
    gap: 14px;
  }
  .front__tab {
    position: absolute; left: 0; top: 30px; width: 12px; height: 150px;
    background: var(--blue-deep);
    border-radius: 0 3px 3px 0;
  }
  .mascot {
    width: 120px; height: 86px; border-radius: 44px;
    background: radial-gradient(circle at 50% 45%, #bfe8f7, #e4f5fb);
  }
  .card--back .mascot {
    width: 150px; height: 110px;
    background: radial-gradient(circle at 50% 45%, #1b5e77, #0f2a35);
  }
  .brand-name {
    color: var(--brand-blue);
    font-size: 17px;
    text-align: center;
    line-height: 1.3;
  }

  /* front: info side */
  .front__info-side {
    position: absolute; right: 0; top: 0; width: 320px; height: 100%;
    background: linear-gradient(160deg, var(--blue-light), var(--blue-deep));
    color: var(--ink-white);
    padding: 34px 28px 0 30px;
  }
  .person-name { font-size: 31px; font-weight: 400; letter-spacing: 0.3px; margin-bottom: 16px; }
  .contact-list { list-style: none; font-size: 14px; line-height: 1.55; }
  .contact-list li { display: flex; align-items: flex-start; gap: 9px; }
  .contact-icon {
    flex: 0 0 14px; height: 14px; margin-top: 4px;
    background: var(--ink-white); border-radius: 2px;
    display: flex; align-items: center; justify-content: center;
  }
  .contact-icon svg { width: 10px; height: 10px; fill: var(--blue-deep); }
  .tagline { font-size: 14px; line-height: 1.45; margin-top: 16px; }

  /* back */
  .back__content {
    position: absolute; inset: 0;
    display: flex; flex-direction: column; align-items: center; justify-content: center; gap: 16px;
  }
  .card--back .brand-name { font-size: 22px; }
</style>
</head>
<body>

<section class="card card--front" aria-label="Business card front">
  <div class="front__tab"></div>
  <div class="front__logo-side">
    <div class="mascot" role="img" aria-label="Cartoon fish mascot illustration in light blue line art"></div>
    <p class="brand-name">Tall Cedar Technology</p>
  </div>
  <div class="front__info-side">
    <h1 class="person-name">Daniel Reyes</h1>
    <ul class="contact-list">
      <li>
        <span class="contact-icon"><svg viewBox="0 0 10 10"><path d="M2 1l2 2-1 1.2c.6 1.2 1.6 2.2 2.8 2.8L7 6l2 2-1.2 1.2C4.5 9 1 5.5.8 2.2z"/></svg></span>
        <span>480-555-0147</span>
      </li>
      <li>
        <span class="contact-icon"><svg viewBox="0 0 10 10"><circle cx="5" cy="5" r="4" fill="none" stroke="#0a78b8" stroke-width="1.2"/><path d="M1 5h8M5 1c-2 2.5-2 5.5 0 8M5 1c2 2.5 2 5.5 0 8" fill="none" stroke="#0a78b8" stroke-width="0.8"/></svg></span>
        <span>www.tallcedar.com</span>
      </li>
      <li>
        <span class="contact-icon"><svg viewBox="0 0 10 10"><path d="M5 1L1 5h1.3v4h2V6.5h1.4V9h2V5H9z"/></svg></span>
        <span>2210 N.Harbor Lane tempe,<br>Arizona 85281</span>
      </li>
    </ul>
    <p class="tagline">Also maybe our tagline which is<br>"hooked on technology"</p>
  </div>
</section>

<section class="card card--back" aria-label="Business card back">
  <div class="back__content">
    <div class="mascot" role="img" aria-label="Cartoon fish mascot illustration in bright blue line art"></div>
    <p class="brand-name">Tall Cedar Technology</p>
  </div>
</section>

</body>
</html>
```